We need a flyer designed for our 4th Annual Harvestlight: A Kinfolk Gathering of Heritage Festival that includes the day, time, location, address, and logos. It also needs to include what to expect. The event will be held on Saturday June 14th from 12p-6p at Gallery Commons located at 418 N. Belcourt Ave., Pensacola, FL 32507. Please see uploaded files for prior flyers for reference when it comes to information to include. Also I've uploaded pictures from our prior festivals that you may incorporate and logos.

```html
<!DOCTYPE html>
<html lang="en">
<head>
<meta charset="utf-8">
<title>4th Annual Harvestlight Festival Flyer</title>
<link rel="stylesheet" href="https://fonts.googleapis.com/css2?family=Oswald:wght@400;500;600&family=Montserrat:wght@800;900&family=Barlow:wght@500&display=swap">
<style>
  :root{
    --green:#247a55;
    --gold:#fbbd12;
    --orange:#f39a12;
    --red:#d4161d;
    --ink:#333333;
    --ink-dark:#1e1e1e;
    --paper:#ffffff;
    --brown:#6e4129;
    --peach:#fd8b5f;
  }
  *{margin:0;padding:0;box-sizing:border-box}
  html,body{width:849px;height:1200px;overflow:hidden;background:var(--paper)}
  .flyer{position:relative;width:849px;height:1200px;overflow:hidden;background:var(--paper)}
  .stripe{position:absolute;top:0;height:1200px}
  .stripe--green-l{left:0;width:79px;background:var(--green)}
  .stripe--gold-l{left:79px;width:63px;background:linear-gradient(90deg,var(--gold),var(--orange))}
  .stripe--red-l{left:142px;width:59px;background:var(--red)}
  .stripe--red-r{left:651px;width:59px;background:var(--red)}
  .stripe--gold-r{left:710px;width:65px;background:linear-gradient(90deg,var(--orange),var(--gold))}
  .stripe--green-r{left:775px;width:74px;background:var(--green)}

  .bunting{position:absolute;left:201px;top:0;width:450px;height:187px;
    background:linear-gradient(180deg,rgba(251,189,18,.35),rgba(212,22,29,.25) 50%,rgba(36,122,85,.25));}
  .hands{position:absolute;left:201px;top:198px;width:450px;height:148px;
    background:linear-gradient(90deg,var(--brown) 0%,#9a5a3a 45%,#e07a52 55%,var(--peach) 100%);}

  .center{position:absolute;left:201px;width:450px;text-align:center}
  .presents{top:359px;font:500 12.5px/1 'Oswald',sans-serif;color:var(--ink-dark);letter-spacing:.3px}
  .edition{top:380px;font:500 25px/1 'Oswald',sans-serif;color:var(--ink-dark);letter-spacing:.5px}
  .edition sup{font-size:12px;vertical-align:top;position:relative;top:-1px}
  .title-top{top:424px;font:900 68px/1 'Montserrat',sans-serif;color:var(--ink)}
  .tagline{top:496px;font:500 17px/1 'Barlow',sans-serif;color:var(--orange);letter-spacing:1px}
  .title-bottom{top:514px;font:900 74px/1 'Montserrat',sans-serif;color:var(--ink)}
  .pillars{top:587px;font:600 22px/1 'Oswald',sans-serif;letter-spacing:.3px}
  .pillars .c1{color:var(--green)} .pillars .c2{color:var(--orange)} .pillars .c3{color:var(--red)}
  .dot{display:inline-block;width:6px;height:6px;border-radius:50%;margin:0 8px;vertical-align:middle;background:var(--orange)}
  .dot--red{background:var(--red)}

  .date{top:652px;display:flex;justify-content:center;align-items:flex-start;gap:14px;color:var(--red)}
  .date__words{text-align:left;font-family:'Montserrat',sans-serif;font-weight:900}
  .date__day{font-size:21px;line-height:1;margin-top:6px}
  .date__month{font-size:44px;line-height:1}
  .date__num{font:900 86px/.85 'Montserrat',sans-serif;letter-spacing:-2px}
  .date__num sup{font-size:46px;vertical-align:top;position:relative;top:-4px;margin-left:4px}
  .time{top:725px;font:400 46px/1 'Oswald',sans-serif;color:var(--ink-dark)}

  .expect-head{top:802px;font:600 29px/1 'Oswald',sans-serif;color:var(--green)}
  .expect-list{top:834px;font:400 15.5px/21.5px 'Oswald',sans-serif;color:var(--ink-dark)}
  .gem{display:inline-block;width:7px;height:7px;transform:rotate(45deg);margin:0 6px 2px;vertical-align:middle}
  .gem--g{background:var(--green)} .gem--o{background:var(--orange)} .gem--r{background:var(--red)}

  .venue{top:927px;font:900 38px/1 'Montserrat',sans-serif;color:var(--orange)}
  .address{top:967px;font:800 19.5px/27px 'Montserrat',sans-serif;color:var(--ink-dark)}

  .sponsor{position:absolute;left:348px;top:1041px;width:292px;height:68px;display:flex;align-items:center;justify-content:center;
    font:600 23px/1 'Oswald',sans-serif;color:var(--ink-dark);letter-spacing:.5px}
  .host__mark{position:absolute;left:246px;top:1098px;width:62px;height:62px;border-radius:50%;background:var(--gold)}
  .host__name{position:absolute;left:348px;top:1122px;width:292px;text-align:center;
    font:600 25px/26px 'Oswald',sans-serif;color:var(--ink-dark);letter-spacing:.5px}
</style>
</head>
<body>
<main class="flyer">
  <div class="stripe stripe--green-l"></div>
  <div class="stripe stripe--gold-l"></div>
  <div class="stripe stripe--red-l"></div>
  <div class="stripe stripe--red-r"></div>
  <div class="stripe stripe--gold-r"></div>
  <div class="stripe stripe--green-r"></div>

  <div class="bunting" role="img" aria-label="Colourful festive pennant bunting strung across the top"></div>
  <div class="hands" role="img" aria-label="Two hands of different skin tones forming a heart, wearing beaded bracelets"></div>

  <p class="center presents">THE CALDER FAMILY FOUNDATION PRESENTS</p>
  <p class="center edition">THE 4<sup>TH</sup> ANNUAL HARVESTLIGHT:</p>
  <h1 class="center title-top">HARVEST</h1>
  <p class="center tagline">A KINFOLK GATHERING OF HERITAGE</p>
  <p class="center title-bottom">LIGHT</p>
  <p class="center pillars"><span class="c1">COMMUNITY</span><span class="dot"></span><span class="c2">ARTS</span><span class="dot dot--red"></span><span class="c3">CULTURE</span></p>

  <div class="center date">
    <div class="date__words"><div class="date__day">SATURDAY</div><div class="date__month">JUNE</div></div>
    <div class="date__num">14<sup>th</sup></div>
  </div>
  <p class="center time">12:00 PM – 6:00 PM</p>

  <h2 class="center expect-head">WHAT TO EXPECT</h2>
  <p class="center expect-list">
    Live performances<span class="gem gem--g"></span>Food vendors<span class="gem gem--o"></span>Art/African clothing vendor<br>
    <span class="gem gem--r"></span>Kids obstacle course &amp; play area<span class="gem gem--g"></span>Spades &amp; domino tables<br>
    <span class="gem gem--o"></span>Bring your own chairs or picnic blankets
  </p>

  <h2 class="center venue">GALLERY COMMONS</h2>
  <p class="center address">418 N. BELCOURT AVE.<br>PENSACOLA, FL 32507</p>

  <p class="sponsor">MARLOWE LAW GROUP, PLLC</p>
  <span class="host__mark"></span>
  <p class="host__name">THE CALDER FAMILY<br>FOUNDATION</p>
</main>
</body>
</html>
```